Office brochure for chronic pain doctor

I need an brochure for my office, and since I want to be able to mail the brochure, I think trifold would be the best size. I treat patients with chronic head and neck pain, as well as sleep apnea. I treat all of the following:

1. headaches
2. myofascial pain, which is a fancy way of saying muscle pain
3. neuropathic pain, which is a fancy way of saying nerve pain
4. TMJ, which stands for the temporomandibular joint (jaw joint)
5. obstructive sleep apnea

The colors will be based on my logo on my website, which you can see at www.BrightJPR.net, and you can learn more about what I do at my website. JPR stands for orofacial pain, which is a speciality training within the field of dentistry but I do not treat teeth. I have high resolution graphics for the brochure so I need someone with an artistic eye to design and lay out the brochure.

The logo colors are:
Purple 9e80bb
Pink f6b1d0
Blue 0f4b8f
Updates

I had a request for the logo in a .ai or .pdf format, which I have just uploaded. Please let me know if you have any other requests. Thank you, Dale

Target Market(s)

80% female, 20% male. I am in an upscale area of Los Angeles called Crestview Hills but I will see a patient from any area around Los Angeles or from any area in the world.

Industry/Entity Type

Training

Colors
6b449b
e567a6
0355a3

Requirements
Must have
• I want a small section of the brochure to feature each of the five areas I treat, and I have included an image to place in each of the five sections. A small section should include a short bio of me, which you can condense from www.brightjpr.net/dale. The brochure must appeal to women since 80% of my patients are female but I don't want to completely ignore men. Most of the pain patients are female, and most of the sleep apnea patients are male.

Here are the colors in my logo
Purple 9e80bb
Pink f6b1d0
Blue 0f4b8f
Should not have
• Anything related to teeth or dentistry.
No decorative or script fonts.

```html
<!DOCTYPE html>
<html lang="en">
<head>
<meta charset="utf-8">
<title>BrightJPR Trifold Brochure</title>
<link href="https://fonts.googleapis.com/css2?family=Cinzel:wght@500&family=Didact+Gothic&family=Signika:wght@500;600&display=swap" rel="stylesheet">
<style>
:root{
  --pink:#f6b1d0;
  --purple:#9e80bb;
  --blue:#0f4b8f;
  --navy:#1c3f8a;
  --text:#444a55;
  --paper-top:#ffffff;
  --paper-bottom:#e3e7ef;
  --photo-warm:#e9d6c8;
  --photo-cool:#dfe3ea;
}
*{box-sizing:border-box;margin:0;padding:0}
html,body{width:1200px;height:930px;overflow:hidden;background:#fff}
.brochure{position:relative;width:1200px;height:930px;font-family:"Didact Gothic",sans-serif;color:var(--text)}
.panel{position:absolute;top:0;width:400px;height:930px;background:linear-gradient(180deg,var(--paper-top) 0%,var(--paper-bottom) 100%);overflow:hidden}
.panel--bio{left:0}
.panel--contact{left:400px;border-left:1px solid #cfd3dc}
.panel--services{left:800px;border-left:1px solid #cfd3dc}
.bar{position:absolute;left:0;bottom:0;width:100%;height:24px}
.bar--purple{background:var(--purple)}
.bar--blue{background:var(--blue)}
.band{position:absolute;background:var(--pink)}
.photo{position:absolute;border-radius:6px;box-shadow:0 2px 6px rgba(0,0,0,.25)}

/* Bio panel */
.bio-band{left:0;top:280px;width:400px;height:164px}
.portrait{left:81px;top:43px;width:239px;height:267px;background:linear-gradient(160deg,#4e5c5b 0%,#3b4848 45%,#e9ecf1 46%,#dfe3ea 100%);border-radius:10px}
.doctor-name{position:absolute;left:0;top:325px;width:400px;text-align:center;font-family:"Signika",sans-serif;font-weight:600;font-size:28px;line-height:37px;color:var(--navy)}
.bio{position:absolute;left:33px;top:460px;width:331px;font-size:12.2px;line-height:14.5px;text-align:justify}
.bio p{margin-bottom:14.5px}
.bio p:last-child{margin-bottom:0}
.bio-phone{position:absolute;right:34px;top:873px;font-family:"Signika",sans-serif;font-weight:600;font-size:25px;line-height:30px;color:var(--navy);display:flex;align-items:center;gap:4px}

/* Contact panel */
.tagline{position:absolute;left:0;top:62px;width:400px;text-align:center;font-family:"Cinzel",serif;font-weight:500;font-size:30px;line-height:37px;color:var(--navy)}
.contact-band{left:0;top:280px;width:200px;height:164px}
.diamond{position:absolute;left:484px;top:246px;width:232px;height:232px;background:#fff;border-radius:46px;transform:rotate(45deg);box-shadow:0 3px 10px rgba(0,0,0,.12)}
.contact-card{position:absolute;left:400px;top:290px;width:400px;text-align:center;color:var(--navy);font-size:13.5px;line-height:17px}
.brand{display:inline-flex;align-items:center;gap:7px;font-family:"Signika",sans-serif;font-weight:600;color:var(--blue)}
.brand-square{display:inline-block;background:var(--purple)}
.contact-card .brand{font-size:20px;margin-bottom:14px}
.contact-card .brand-square{width:16px;height:16px}
.contact-line{display:flex;justify-content:center;align-items:center;gap:4px}
.contact-line.gap{margin-top:10px}
.contact-line.strong{font-weight:bold;font-family:"Signika",sans-serif;font-size:15px}
.map{left:442px;top:565px;width:319px;height:274px;background:linear-gradient(135deg,#e6e3dc 0%,#dcd9d1 100%);border-radius:2px}
.social{position:absolute;left:400px;top:860px;width:400px;display:flex;justify-content:center;gap:7px}
.social span{width:39px;height:39px;border-radius:50%;display:flex;align-items:center;justify-content:center;color:#fff;font-size:9.5px;font-family:"Signika",sans-serif;font-weight:600;box-shadow:0 1px 3px rgba(0,0,0,.3)}
.s1{background:#3aa3dd}.s2{background:#d8312a}.s3{background:#d9432f}.s4{background:#f08a24}.s5{background:#c41a1a}

/* Services panel */
.panel--services .brand{position:absolute;left:0;top:82px;width:400px;justify-content:center;font-size:34px}
.panel--services .brand-square{width:38px;height:38px;background:var(--pink)}
.ph-1{left:15px;top:187px;width:181px;height:181px;background:linear-gradient(180deg,#f0e6e0,var(--photo-warm))}
.ph-2{left:207px;top:187px;width:181px;height:181px;background:linear-gradient(180deg,#eef0f3,var(--photo-warm))}
.ph-3{left:15px;top:422px;width:181px;height:181px;background:linear-gradient(180deg,#eef0f3,#b9c79a)}
.ph-4{left:207px;top:422px;width:181px;height:181px;background:linear-gradient(180deg,#ecedf0,var(--photo-cool))}
.ph-5{left:16px;top:658px;width:370px;height:164px;background:linear-gradient(180deg,#e9ecf2,#d8d6d3)}
.service-band{left:0;width:400px;height:35px;display:flex;align-items:center;font-family:"Signika",sans-serif;font-weight:500;font-size:21px;color:var(--navy)}
.service-band span{width:50%;text-align:center}
.sb-1{top:375px}.sb-2{top:610px}
.sb-3{top:829px;height:33px;justify-content:center;font-size:24px}
.web{position:absolute;left:0;top:878px;width:400px;text-align:center;font-size:17px;letter-spacing:2.5px;color:var(--navy)}
</style>
</head>
<body>
<main class="brochure">

  <section class="panel panel--bio">
    <div class="band bio-band"></div>
    <div class="photo portrait" role="img" aria-label="Portrait photograph of the doctor in a white coat"></div>
    <h1 class="doctor-name">Dr. Dale Marston<br>Crestview Hills<br>Facial Pain Doctor</h1>
    <div class="bio">
      <p>I have lived in Crestview Hills since 1993, I wanted to practice locally, and was fortunate to find a great location at the corner of Larkspur Way and Alder Drive, in the Sterling Court building, which is where Casa Lumina, the restaurant owned by Marisa Delane, is located. It is a great building, and I have tried to create a unique office to help patients suffering from chronic head and neck pain. If you are suffering from migraine headaches, cluster headaches, morning headaches, head and neck muscle pain, sharp shooting electrical type of pain in your head or neck, TMJ (or what you have been told is TMJ), or snoring and/or obstructive sleep apnea, please make an appointment at my Crestview Hills chronic pain office for me to examine you to see if I can help manage or eliminate your pain. I promise, I will not even consider drilling your teeth or intentionally try to change your bite to help reduce your pain!</p>
      <p>If you are a dentist, and are interesting in hearing me speak, please know that I have presented at small study clubs, local dental societies, and annual state dental association meetings, and from groups as small as 20 to an audience as large as 2,000. Here are some good testimonials to read from other dentists so please let me know if you are interested in hearing me speak. I guarantee that I will make you think!</p>
      <p>And, yes, I still ride my bike. That is something I don't want to change.</p>
    </div>
    <div class="bio-phone">
      <svg width="24" height="24" viewBox="0 0 24 24" aria-hidden="true"><circle cx="12" cy="12" r="10.5" fill="none" stroke="#9e80bb" stroke-width="1.5"/><path d="M8.5 6.5l2 2-1.2 1.6c.7 1.6 2 2.9 3.6 3.6l1.6-1.2 2 2-1.3 1.8c-3.8-.4-7.1-3.7-7.5-7.5z" fill="none" stroke="#9e80bb" stroke-width="1.3"/></svg>
      (888) 555-0142
    </div>
    <div class="bar bar--purple"></div>
  </section>

  <section class="panel panel--contact">
    <h2 class="tagline">Caring for<br>Head Pain and<br>Sleep Apnea</h2>
    <div class="band contact-band"></div>
    <div class="photo map" role="img" aria-label="Street map showing the office location near the boulevard"></div>
    <div class="bar bar--blue"></div>
  </section>

  <div class="diamond"></div>
  <div class="contact-card">
    <div class="brand"><span class="brand-square"></span>BrightJPR</div>
    <div class="contact-line">
      <svg width="10" height="13" viewBox="0 0 10 13" aria-hidden="true"><path d="M5 12.5S1 7.5 1 4.8a4 4 0 0 1 8 0C9 7.5 5 12.5 5 12.5z" fill="#9e80bb"/><circle cx="5" cy="4.8" r="1.5" fill="#fff"/></svg>
      4820 Larkspur Way Suite 210
    </div>
    <div class="contact-line">Crestview Hills, California 90418</div>
    <div class="contact-line gap strong">
      <svg width="16" height="16" viewBox="0 0 24 24" aria-hidden="true"><circle cx="12" cy="12" r="10.5" fill="none" stroke="#9e80bb" stroke-width="1.8"/><path d="M8.5 6.5l2 2-1.2 1.6c.7 1.6 2 2.9 3.6 3.6l1.6-1.2 2 2-1.3 1.8c-3.8-.4-7.1-3.7-7.5-7.5z" fill="none" stroke="#9e80bb" stroke-width="1.5"/></svg>
      (888) 555-0142
    </div>
    <div class="contact-line">
      <svg width="14" height="12" viewBox="0 0 14 12" aria-hidden="true"><rect x="1" y="5" width="12" height="6" fill="none" stroke="#9e80bb"/><rect x="3.5" y="1" width="7" height="4" fill="none" stroke="#9e80bb"/></svg>
      (310) 555-0187
    </div>
    <div class="contact-line gap">
      <svg width="14" height="10" viewBox="0 0 14 10" aria-hidden="true"><rect x=".5" y=".5" width="13" height="9" fill="none" stroke="#9e80bb"/><path d="M.5.5L7 6l6.5-5.5" fill="none" stroke="#9e80bb"/></svg>
      relief@brightjpr.net
    </div>
    <div class="contact-line" style="margin-top:4px">
      <svg width="12" height="12" viewBox="0 0 12 12" aria-hidden="true"><circle cx="6" cy="6" r="5.3" fill="none" stroke="#9e80bb"/><path d="M.7 6h10.6M6 .7c-2.5 3-2.5 7.6 0 10.6M6 .7c2.5 3 2.5 7.6 0 10.6" fill="none" stroke="#9e80bb" stroke-width=".8"/></svg>
      www.BrightJPR.net
    </div>
  </div>
  <nav class="social" aria-label="Social links">
    <span class="s1">Chirp</span><span class="s2">Vidra</span><span class="s3">Plusly</span><span class="s4">Blogo</span><span class="s5">Rately</span>
  </nav>

  <section class="panel panel--services">
    <div class="brand"><span class="brand-square"></span>BrightJPR</div>
    <div class="photo ph-1" role="img" aria-label="Photo of a woman holding her temples with a headache"></div>
    <div class="photo ph-2" role="img" aria-label="Photo of a woman rubbing a sore neck and shoulder"></div>
    <div class="band service-band sb-1"><span>HEADACHES</span><span>MYOFASCIAL PAIN</span></div>
    <div class="photo ph-3" role="img" aria-label="Photo of an older woman holding her face in nerve pain"></div>
    <div class="photo ph-4" role="img" aria-label="Photo of a woman holding her jaw in pain"></div>
    <div class="band service-band sb-2"><span>NEUROPATHIC PAIN</span><span>TMJ</span></div>
    <div class="photo ph-5" role="img" aria-label="Photo of a man snoring in bed while his partner covers her ears"></div>
    <div class="band service-band sb-3">OBSTRUCTIVE SLEEP APNEA</div>
    <div class="web">
      <svg width="15" height="15" viewBox="0 0 12 12" aria-hidden="true" style="vertical-align:-2px"><circle cx="6" cy="6" r="5.3" fill="none" stroke="#9e80bb"/><path d="M.7 6h10.6M6 .7c-2.5 3-2.5 7.6 0 10.6M6 .7c2.5 3 2.5 7.6 0 10.6" fill="none" stroke="#9e80bb" stroke-width=".8"/></svg>
      www.BrightJPR.net
    </div>
    <div class="bar bar--purple"></div>
  </section>

</main>
</body>
</html>
```